Psychology Practice Brochure and Letterhead
Quiet Harbor Psychological Services
I will have a submission in very shortly.
Sorry for the omission of our business contact information:
26840 W. 93rd St., Suite 410
Denbury Glen, IL 60512
Phone/Fax: 708.519.2483
info@quietharborpsych.example
#2,#7 and #8
*****Please note that we have shortened the "what to expect" section and alphabetized the items under the "what we treat" section. The new wording has been uploaded and is in the brief, along with some pictures and quotes we would like you to incorporate.
Thank you so much for your hard work on our project! We really like the green curved lines of #8 because it ties all the sections together. Could you put the "do i need therapy" section on the left outside panel? Then, you can move the "what to expect" section to the middle section with a map. Also, we really like the different shades of blue that you put behind the different text sections of #2 because it makes it easier to read.Thanks
Hello designers! We are so excited about your creative ideas for the brochure.
*****Please note that we have changed the brochure wording slightly, so please edit the text in your submissions. The changes are as follows:
1) The bullet points under "What we treat" have now been alphabetized.
2)We have shortened the "what to expect" section so that it fits better with the map on the back page of the brochure. These changes are reflected in the uploaded file called "new brochure wording."
Hello designers. Please see our design brief, as we have recently uploaded photos for you to include in the brochure. Below are some quotes that we like. Feel free to include one or two in the brochure.
"A journey of a thousand miles begins with a single step." Wen Shaoli
"I am not what happens to me, I am what I choose to become." Emil Dorst
"Life is not about who you once were, it is about who you are right now, and the person you have the potential to become." Unknown
We have identified a number of photos and quotes from various sites that we might want to use, but don't want to buy them all in case they don't ultimately work in the design. Is it ok to upload them, but then buy them if they are used?
Drafts #2 and #5: Could you incorporate both blue and green?
draft #5: thank you for your submission. Could we see the design without the pictures of physicians in lab coats? Instead, we would like to see pictures of adults, children or families. Having some pictures of people looking unhappy, angry or stressed is fine along with happier pictures, as well. Any quotes about happiness or hopefulness would also be welcome.
draft #2: Thank you for your submission. Could you replace the picture of the older couple and replace it with children or teens? Also, could you show us another option for the layout on the interior? Or, another way of separating the sections that doesn't use the solid lines?
draft #1: Thank you for your submission. We like the way you've used blue and green throughout the brochure, and the addition of the tree was nice. Is there a way to reduce the quantity of brown used? Also, could you give us some additional variety in the pictures used, such as some in which the people are not jumping?
Do you have any website?
we need vector logo! please upload it!

```html
<!DOCTYPE html>
<html lang="en">
<head>
<meta charset="utf-8">
<title>Quiet Harbor Psychological Services – Brochure and Letterhead</title>
<link href="https://fonts.googleapis.com/css2?family=Crimson+Text:ital,wght@0,400;0,600;1,400&family=Open+Sans:wght@400;600;700&display=swap" rel="stylesheet">
<style>
:root{
  --bg:#e9e6e1;
  --teal-deep:#0a3f52;
  --teal:#0f5a72;
  --blue:#1e7ea5;
  --blue-soft:#cfe6f0;
  --blue-pale:#e8f4f9;
  --green:#6cb832;
  --green-dark:#3f8a1c;
  --ink:#20323a;
  --white:#ffffff;
  --label:#5a5048;
}
*{box-sizing:border-box;margin:0;padding:0}
html,body{width:1200px;height:901px;overflow:hidden}
body{background:var(--bg);font-family:"Open Sans",Arial,sans-serif;color:var(--ink);position:relative}
.piece{position:absolute;overflow:hidden;box-shadow:0 2px 6px rgba(0,0,0,.25)}
.piece-label{position:absolute;font-size:12px;color:var(--label)}
.photo{position:absolute}
.tiny{font-size:5.2px;line-height:1.45}
.heading{font-family:"Crimson Text",Georgia,serif;font-weight:600}
.brand{font-family:"Open Sans",Arial,sans-serif;font-weight:700;color:var(--blue);display:flex;align-items:center;gap:6px}
.brand .dot{width:12px;height:12px;border-radius:50%;background:var(--green)}

/* outside brochure */
.outside{left:34px;top:12px;width:554px;height:420px;background:var(--teal)}
.outside .panel{position:absolute;top:0;height:100%;width:184.6px}
.panel-therapy{left:0;background:var(--teal-deep);color:var(--white)}
.panel-expect{left:184.6px;background:var(--teal);color:var(--white)}
.panel-cover{left:369.2px;background:var(--white)}
.panel-therapy .title{position:absolute;left:10px;right:10px;top:148px;font-size:22px;line-height:1.05;color:var(--white)}
.panel-therapy .body{position:absolute;left:10px;right:10px;top:212px;color:#d9ecf2}
.panel-expect .title{position:absolute;left:14px;top:12px;font-size:15px}
.panel-expect .body{position:absolute;left:14px;right:12px;top:36px;color:#e3f1f6}
.panel-expect .cta{position:absolute;left:14px;right:12px;top:130px;font-family:"Crimson Text",Georgia,serif;font-size:14px;line-height:1.2;text-align:center;color:var(--white)}
.contact-box{position:absolute;left:10px;right:10px;top:214px;height:56px;background:var(--white);color:var(--ink);padding:6px 8px}
.contact-box .phone{font-size:10px;font-weight:700;color:var(--teal-deep)}
.contact-box .addr{font-size:6px;line-height:1.45;margin-top:2px}
.map-area{position:absolute;left:10px;right:10px;top:278px;height:128px;background:linear-gradient(135deg,#e4e2d6,#cfd8c5)}
.panel-cover .quote{position:absolute;left:14px;right:14px;top:222px;font-family:"Crimson Text",Georgia,serif;font-style:italic;font-size:13px;line-height:1.2;color:var(--white)}
.panel-cover .quote small{display:block;text-align:right;font-size:8px;margin-top:3px}
.cover-brand{position:absolute;left:0;right:0;top:330px;text-align:center}
.cover-brand .brand{justify-content:center;font-size:18px}
.cover-brand .sub{font-size:6.5px;letter-spacing:1.5px;color:var(--teal);margin-top:4px;text-transform:uppercase}

/* inside brochure */
.inside{left:34px;top:449px;width:554px;height:427px;background:var(--blue-pale)}
.philosophy{position:absolute;left:0;top:0;width:100%;height:90px;background:var(--teal-deep);color:var(--white);padding:8px 14px}
.philosophy .title{font-size:15px}
.philosophy .tiny{color:#d5e8ef;margin-top:3px}
.help{position:absolute;left:0;top:90px;width:370px;height:170px;background:var(--blue-soft);padding:10px 14px}
.help .title{font-size:15px;color:var(--green-dark)}
.help .tiny{margin-top:3px}
.help b{color:var(--teal)}
.help-photo{left:370px;top:90px;width:184px;height:170px;background:linear-gradient(160deg,#bcd9e6,#8fb9c9 55%,#5d8a6a)}
.help-quote{position:absolute;left:382px;top:100px;width:160px;font-family:"Crimson Text",Georgia,serif;font-style:italic;font-size:9px;line-height:1.25;color:var(--white)}
.treat{position:absolute;left:0;top:260px;width:100%;height:167px;background:var(--white)}
.treat-photo{left:0;top:0;width:120px;height:167px;background:linear-gradient(180deg,#d7dee2,#9fb3bd)}
.treat .title{position:absolute;left:134px;top:10px;font-size:15px;color:var(--green-dark)}
.treat .lead{position:absolute;left:134px;top:34px;right:14px}
.treat-list{position:absolute;left:134px;top:56px;right:14px;display:grid;grid-template-columns:1fr 1fr;column-gap:16px;list-style:none;font-size:6px;line-height:1.7}
.treat-list li::before{content:"•";color:var(--green);margin-right:4px}

/* front fold */
.front-fold{left:648px;top:12px;width:168px;height:196px;background:var(--white)}
.front-fold .brand{position:absolute;left:0;right:0;bottom:26px;justify-content:center;font-size:14px}

/* letterhead */
.letterhead{left:660px;top:230px;width:384px;height:590px;background:var(--white)}
.letterhead .brand{position:absolute;left:22px;top:26px;font-size:19px}
.letterhead .brand-sub{position:absolute;left:40px;top:52px;font-size:6px;letter-spacing:1.4px;color:var(--teal);text-transform:uppercase}
.lh-contact{position:absolute;right:22px;top:24px;text-align:right;font-size:6px;line-height:1.5;color:var(--ink)}
.lh-contact .phone{font-size:11px;font-weight:700;color:var(--teal-deep)}
.lh-list{position:absolute;left:22px;right:22px;bottom:22px;display:grid;grid-template-columns:1fr 1fr;column-gap:20px;list-style:none;font-size:5.4px;line-height:1.6;color:var(--blue)}
</style>
</head>
<body>

<!-- Outside brochure -->
<section class="piece outside" aria-label="Outside brochure">
  <div class="panel panel-therapy">
    <div class="photo" role="img" aria-label="Photo of a stressed woman holding her head" style="left:0;top:0;width:184.6px;height:200px;background:linear-gradient(170deg,#c9d3d6,#8fa3ab 60%,#3e6070)"></div>
    <h2 class="heading title">Do I Need<br>Therapy?</h2>
    <div class="body tiny">
      <p>Most people experience problems at some point in life, but how do you know when to seek help from a professional?</p>
      <p style="margin-top:4px">• Your worries feel heavier than they used to and do not pass.<br>• You are losing sleep, appetite or interest in things you enjoy.<br>• Family, school or work feel harder every single week.<br>• Friends or loved ones have told you they are concerned.<br>• You feel "stuck" and cannot see a way forward alone.</p>
      <p style="margin-top:4px">Whether you are struggling with a particular issue or simply want to feel better, our caring team is here to listen and help you find a path forward.</p>
    </div>
  </div>

  <div class="panel panel-expect">
    <h2 class="heading title">What To Expect</h2>
    <p class="body tiny">During the first session, your clinician will get to know you and your concerns. Together you will set goals and discuss a plan that fits your needs. Sessions are private, respectful and paced for you. Most clients meet weekly and notice progress within a few months of steady work.</p>
    <p class="cta">Take the first step toward a better tomorrow and give us a call today.</p>
    <div class="contact-box">
      <div class="phone">Phone/Fax 708.519.2483</div>
      <div class="addr">info@quietharborpsych.example<br>Quiet Harbor Psychological Services<br>26840 W. 93rd St., Suite 410, Denbury Glen, IL 60512</div>
    </div>
    <div class="map-area" role="img" aria-label="Street map showing the office location"></div>
  </div>

  <div class="panel panel-cover">
    <div class="photo" role="img" aria-label="Photo of a happy child jumping outdoors" style="left:0;top:0;width:184.6px;height:310px;background:linear-gradient(180deg,#8cc7e6,#5aa6d2 55%,#d9a25a 80%,#7fae4a)"></div>
    <svg class="photo" style="left:0;top:280px" width="185" height="40" viewBox="0 0 185 40" aria-hidden="true">
      <path d="M0 30 Q90 0 185 18 L185 40 L0 40Z" fill="#ffffff"/>
      <path d="M0 30 Q90 0 185 18" fill="none" stroke="#6cb832" stroke-width="3"/>
    </svg>
    <p class="quote">“A journey of a thousand miles begins with a single step.”<small>– Wen Shaoli</small></p>
    <div class="cover-brand">
      <div class="brand"><span class="dot"></span>Quiet Harbor</div>
      <div class="sub">Psychological Services</div>
    </div>
  </div>
</section>
<span class="piece-label" style="left:600px;top:312px">Outside<br>Brochure</span>

<!-- Front fold -->
<section class="piece front-fold" aria-label="Front fold">
  <div class="photo" role="img" aria-label="Photo of a happy child jumping outdoors" style="left:0;top:0;width:168px;height:140px;background:linear-gradient(180deg,#8cc7e6,#5aa6d2 55%,#d9a25a 80%,#7fae4a)"></div>
  <svg class="photo" style="left:0;top:118px" width="168" height="30" viewBox="0 0 168 30" aria-hidden="true">
    <path d="M0 24 Q80 0 168 14 L168 30 L0 30Z" fill="#ffffff"/>
    <path d="M0 24 Q80 0 168 14" fill="none" stroke="#6cb832" stroke-width="3"/>
  </svg>
  <div class="brand"><span class="dot"></span>Quiet Harbor</div>
</section>
<span class="piece-label" style="left:826px;top:190px">Front Fold</span>

<!-- Inside brochure -->
<section class="piece inside" aria-label="Inside brochure">
  <div class="philosophy">
    <h2 class="heading title">Philosophy</h2>
    <p class="tiny">Sometimes we all need a little help getting through life's challenges. At Quiet Harbor Psychological Services, we provide a supportive, nonjudgmental environment where clients feel welcome and respected. We believe in empowering our clients and in building collaborative relationships with each person we see. By offering insight into core problems and teaching practical skills, we help clients move toward healthier choices and stronger relationships with others. Our goal is to help every person discover their own strengths, overcome obstacles and build a brighter future for themselves and their loved ones.</p>
  </div>
  <div class="help">
    <h2 class="heading title">How We Help</h2>
    <p class="tiny">At Quiet Harbor, we have a number of tools to help you and your family achieve your goals.</p>
    <p class="tiny"><b>Individual Therapy:</b> Helps you gain a clearer understanding of the factors contributing to your current difficulties and provides you with new skills to manage them.</p>
    <p class="tiny"><b>Child and Adolescent Therapy:</b> Helps children express their emotions and behaviors and cope with life changes in healthy ways.</p>
    <p class="tiny"><b>Couples Therapy:</b> Explores the complex relationship dynamics that lead to conflict and improves communication and closeness.</p>
    <p class="tiny"><b>Parent Coaching:</b> Increases parents' awareness of the factors influencing their children's behavior and teaches effective ways to respond.</p>
    <p class="tiny"><b>Psychological and Neuropsychological Testing:</b> Clarifies cognitive, emotional and learning concerns and guides the most effective treatment plan.</p>
  </div>
  <div class="photo help-photo" role="img" aria-label="Photo of a smiling family outdoors"></div>
  <p class="help-quote">“Life is not about who you once were, it is about who you are right now, and the person you have the potential to become.”</p>
  <div class="treat">
    <div class="photo treat-photo" role="img" aria-label="Photo of a young woman holding a water bottle"></div>
    <h2 class="heading title">What We Treat</h2>
    <p class="tiny lead">We all need a little help in some areas of life. Our team works with children, teens, adults, couples and families. Some specific problems that we can help with are:</p>
    <ul class="treat-list">
      <li>Anxiety, panic attacks, phobias and obsessive compulsive disorder</li>
      <li>Parenting challenges and support</li>
      <li>Attention deficit hyperactivity disorder</li>
      <li>Personality and behavioral difficulties</li>
      <li>Autism spectrum disorders</li>
      <li>School refusal and learning difficulties</li>
      <li>Child and adolescent emotional concerns</li>
      <li>Self esteem and confidence concerns</li>
      <li>Depression and bipolar disorder</li>
      <li>Stress management and coping skills</li>
      <li>Family or relationship conflict</li>
      <li>Grief, loss and life transitions</li>
    </ul>
  </div>
</section>
<span class="piece-label" style="left:600px;top:780px">Inside<br>Brochure</span>

<!-- Letterhead -->
<section class="piece letterhead" aria-label="Letterhead">
  <div class="brand"><span class="dot"></span>Quiet Harbor</div>
  <div class="brand-sub">Psychological Services</div>
  <div class="lh-contact">
    <div class="phone">708.519.2483</div>
    info@quietharborpsych.example<br>26840 W. 93rd St., Suite 410, Denbury Glen, IL 60512
  </div>
  <svg class="photo" style="left:0;top:70px" width="384" height="40" viewBox="0 0 384 40" aria-hidden="true">
    <path d="M0 30 Q190 2 384 22" fill="none" stroke="#6cb832" stroke-width="3"/>
    <path d="M0 34 Q190 10 384 28" fill="none" stroke="#1e7ea5" stroke-width="1.5"/>
  </svg>
  <ul class="lh-list">
    <li>Anxiety, panic attacks, phobias and obsessive compulsive</li>
    <li>Parenting challenges and support</li>
    <li>Attention deficit hyperactivity disorder</li>
    <li>Personality and behavioral difficulties</li>
    <li>Autism spectrum disorders</li>
    <li>School refusal and learning difficulties</li>
    <li>Child and adolescent emotional concerns</li>
    <li>Self esteem and confidence concerns</li>
    <li>Depression and bipolar disorder</li>
    <li>Stress management and coping skills</li>
  </ul>
</section>
<span class="piece-label" style="left:660px;top:832px">Letterhead</span>

</body>
</html>
```